Custome made to measure suit brochure

Company info
Northern Heron Supply Company Ltd.
Import and export company based in Vancouver BC, Canada.

Project Scope
We need to have a brochure developed that will help us sell our custom made to measure suits from Asia (China and India) to North America.

We are not picky on the number of pages, we are looking for a brochure that best displays the needed information.
We don’t have any pictures taken, we are hoping that stock photos can be used or the winning bid will provide the photos.
Attached is our company logo and name, the attachments has 4 or 5 examples, the logo that is being used is the logo that is red and white only.

Target market is the university or college student and young professionals.
We are looking to sell the suit based on best value. Our suit is 3 to 4 times cheaper than a custom made suit made in North America.
Custom made suits make the wearer look amazing, as compared to an off the rack suit.
Custom made suits are available from $399 and up.
Vests, shirts, pants, skirts, jackets, monogramed, horn buttons, canvas and half canvas suits, pocket squares, silk and paisley linings are all available.
Available in Wool, cotton, linen, and a cotton/cashmere blend
We want the client to call us to set up a free appointment to take their measurements
100% satisfaction or your money back.
Brochure should be easy to read and understand at a quick glance.

Target Market(s)

college, university students and young professionals

Industry/Entity Type

It Company

Contact Information for Business Card

Miles Corvath
President, Northern Heron Supply Company Ltd.
1.604.555.0192
miles@nhsco-example.ca
www.nhsco-example.ca

Font styles to use
Serif

Colors
ec1f27

Requirements
Must have
• easy to read
• professional format

```html
<!DOCTYPE html>
<html lang="en">
<head>
<meta charset="utf-8">
<title>Northern Heron Supply Co – Custom Suit Brochure</title>
<link rel="stylesheet" href="https://fonts.googleapis.com/css2?family=Oswald:wght@400;500;600&family=Open+Sans:wght@400;600&display=swap">
<style>
:root{
  --crimson:#c51a4a;
  --crimson-dark:#a8133d;
  --gold:#ecc94b;
  --paper:#ffffff;
  --paper-soft:#f4f4f6;
  --ink:#4a4a4a;
  --backdrop:#c9c9cb;
  --photo-a:#d9dbe2;
  --photo-b:#9fa3ad;
}
*{box-sizing:border-box;margin:0;padding:0}
html,body{width:1200px;height:1010px;overflow:hidden}
body{background:radial-gradient(ellipse at 50% 45%,#e6e6e7 0%,var(--backdrop) 75%);font-family:"Open Sans",Arial,sans-serif;color:var(--ink);position:relative}
.spread{position:absolute;width:720px;height:466px;display:flex;box-shadow:0 14px 30px rgba(0,0,0,.25)}
.spread--outside{left:40px;top:30px}
.spread--inside{left:440px;top:514px}
.page{position:relative;width:360px;height:466px;overflow:hidden}
.heading{font-family:"Oswald",Arial,sans-serif;font-weight:500;line-height:1.1}
.body-copy{font-size:6.4px;line-height:1.55}
.photo{position:absolute}

/* back panel */
.back{background:var(--crimson);color:#fff}
.store-card{position:absolute;left:12px;top:62px;width:150px;height:246px;background:var(--gold);padding:10px;color:#5a3b00}
.store-card .heading{font-size:15px;color:#333;margin-bottom:6px}
.store-card .photo{position:static;height:70px;margin-bottom:8px;background:linear-gradient(135deg,#8c8f96,#c7c2b8 60%,#6f6a63)}
.store-card .body-copy{color:#5b4a18;margin-bottom:6px}
.history{position:absolute;left:172px;top:28px;width:176px}
.promise{font-size:17px;color:var(--gold);font-weight:600;line-height:1}
.promise span{display:block;font-size:12px}
.history .heading.section{font-size:15px;margin:10px 0 6px}
.history .body-copy{color:#f6d9e1;margin-bottom:7px}
.contact{position:absolute;left:18px;top:338px;width:220px}
.contact .heading{font-size:15px;margin-bottom:10px}
.contact-row{display:flex;align-items:center;gap:9px;font-size:8px;margin-bottom:8px;line-height:1.3}
.contact-row svg{flex:none}

/* cover */
.cover{background:var(--paper)}
.cover-head{position:absolute;left:0;top:0;width:100%;height:58px;background:var(--paper);border-bottom:2px solid var(--crimson);display:flex;align-items:center;justify-content:center;gap:8px;z-index:2}
.brand-dot{width:16px;height:16px;border-radius:50%;background:var(--crimson)}
.brand-name{font-family:"Oswald",Arial,sans-serif;font-weight:500;font-size:14px;color:var(--crimson);line-height:1.05}
.cover .photo{left:0;top:58px;width:100%;height:408px;background:radial-gradient(ellipse at 55% 40%,var(--photo-a),#c3c6ce 55%,#e9eaee)}
.cover-banner{position:absolute;left:26px;top:318px;width:334px;height:112px}
.cover-banner::before{content:"";position:absolute;left:-8px;top:-8px;width:100%;height:100%;background:var(--gold)}
.cover-banner-inner{position:absolute;inset:0;background:var(--crimson);color:#fff;padding:16px 18px}
.cover-banner .heading{font-size:20px;font-weight:400}
.cover-url{font-size:8px;font-weight:600;margin-top:10px}

/* inside left */
.products{background:var(--paper-soft)}
.products .heading.title{position:absolute;left:22px;top:30px;font-size:16px;color:var(--crimson)}
.products-intro{position:absolute;left:22px;top:54px;width:310px}
.product{position:absolute;width:170px}
.product .label{font-family:"Oswald",Arial,sans-serif;font-size:10px;color:#e7a21b;margin-bottom:3px}
.product-1{left:150px;top:92px}
.product-2{left:160px;top:150px}
.product-3{left:40px;top:262px}
.product-4{left:40px;top:322px}
.photo.round{border-radius:50%;border:2px solid var(--crimson)}
.photo-shirt{left:30px;top:118px;width:100px;height:100px;background:radial-gradient(circle at 50% 45%,#8d8f93,#4b4d52 70%,#2e2f33)}
.photo-shoes{left:250px;top:232px;width:100px;height:100px;background:radial-gradient(circle at 50% 50%,#f2f2f2,#9a9a9a 60%,#2a2a2a)}
.fabric-box{position:absolute;left:12px;top:392px;width:170px;height:62px}
.fabric-box::before{content:"";position:absolute;left:-6px;top:-6px;width:100%;height:100%;background:var(--crimson)}
.fabric-box-inner{position:absolute;inset:0;background:var(--gold);display:flex;align-items:center;justify-content:center;text-align:center;font-family:"Oswald",Arial,sans-serif;font-size:11px;color:#222;line-height:1.2;padding:4px 12px}
.testimonial{position:absolute;left:196px;top:392px;width:150px;display:flex;gap:6px}
.testimonial .mark{font-family:"Oswald",Arial,sans-serif;font-size:26px;color:var(--crimson);line-height:.8}
.testimonial .body-copy{color:var(--crimson)}

/* inside right */
.why{background:var(--paper)}
.tagline{position:absolute;left:0;top:32px;width:140px;height:44px}
.tagline::before{content:"";position:absolute;left:6px;top:6px;width:100%;height:100%;background:var(--gold)}
.tagline-inner{position:absolute;inset:0;background:var(--crimson);color:#fff;font-size:6.8px;font-weight:600;padding:8px 10px;line-height:1.35}
.photo-seated{left:176px;top:14px;width:176px;height:86px;background:linear-gradient(90deg,#fff 0%,#b9cbe6 30%,#2f3038 70%,#fff 100%);border-radius:40px}
.why .heading.title{position:absolute;left:22px;top:96px;font-size:15px;color:var(--crimson)}
.reason{position:absolute;left:22px;width:320px;display:flex;gap:12px;align-items:center}
.reason-1{top:124px}.reason-2{top:172px}.reason-3{top:220px}
.reason-icon{flex:none;width:34px;height:34px;border-radius:50%;border:1.5px solid var(--crimson);display:flex;align-items:center;justify-content:center}
.photo-couple{left:20px;top:290px;width:150px;height:150px;background:linear-gradient(180deg,#fff 0%,#c9b7a7 30%,#2b2c30 75%,#fff 100%);border-radius:8px}
.cta{position:absolute;left:178px;top:328px;width:182px;height:100px}
.cta::before{content:"";position:absolute;left:-8px;top:-8px;width:100%;height:100%;background:var(--gold)}
.cta-inner{position:absolute;inset:0;background:var(--crimson);color:#fff;padding:14px 14px;text-align:center}
.cta-lead{font-size:8.5px;font-weight:600;line-height:1.3}
.cta-phone{font-family:"Oswald",Arial,sans-serif;font-size:24px;margin-top:6px}
</style>
</head>
<body>

<section class="spread spread--outside" aria-label="Brochure outside spread">
  <div class="page back">
    <div class="store-card">
      <h2 class="heading">Our Store</h2>
      <div class="photo" role="img" aria-label="Photo of the showroom with suits on display"></div>
      <p class="body-copy">Our showroom lets you feel every fabric before you choose. Our tailors guide each fitting, note your posture and build a pattern that belongs to you alone. Visit us for coffee and a relaxed first consult.</p>
      <p class="body-copy">Bring a favourite jacket and we will match its feel, then improve the fit. Most orders arrive within four weeks.</p>
    </div>
    <div class="history">
      <p class="promise heading">100% SATISFACTION!<span>OR YOUR MONEY BACK.</span></p>
      <h2 class="heading section">Our History</h2>
      <p class="body-copy">We began as a small import house in Vancouver, linking skilled tailors in China and India with clients across North America. Fair prices and honest work have kept us growing ever since.</p>
      <p class="body-copy">Each suit is cut from your own measurements and finished by hand. We check every seam, button and lining before it ships, so your order arrives ready to wear on day one.</p>
      <p class="body-copy">Students and young professionals save three to four times the local price without giving up quality.</p>
    </div>
    <div class="contact">
      <h2 class="heading">Contact Us</h2>
      <div class="contact-row">
        <svg width="10" height="13" viewBox="0 0 10 13"><path d="M5 0a5 5 0 0 0-5 5c0 3.5 5 8 5 8s5-4.5 5-8a5 5 0 0 0-5-5zm0 7a2 2 0 1 1 0-4 2 2 0 0 1 0 4z" fill="#fff"/></svg>
        <span>1420 Harbour Lane #210<br>Vancouver, BC V6B 2K4</span>
      </div>
      <div class="contact-row">
        <svg width="10" height="13" viewBox="0 0 10 13"><rect x="1" y="0.5" width="8" height="12" rx="1.5" fill="none" stroke="#fff"/><circle cx="5" cy="10.5" r=".8" fill="#fff"/></svg>
        <span>(604) 555 0148</span>
      </div>
      <div class="contact-row">
        <svg width="12" height="9" viewBox="0 0 12 9"><rect width="12" height="9" rx="1" fill="#fff"/><path d="M0.5 1 6 5l5.5-4" fill="none" stroke="#c51a4a"/></svg>
        <span>info@nhsco-example.ca</span>
      </div>
    </div>
  </div>

  <div class="page cover">
    <header class="cover-head">
      <span class="brand-dot"></span>
      <span class="brand-name">Northern Heron<br>Supply Co</span>
    </header>
    <div class="photo" role="img" aria-label="Photo of a young man in a black tuxedo with bow tie"></div>
    <div class="cover-banner">
      <div class="cover-banner-inner">
        <h1 class="heading">Custom made suits are available from $399 and up</h1>
        <p class="cover-url">www.nhsco-example.ca</p>
      </div>
    </div>
  </div>
</section>

<section class="spread spread--inside" aria-label="Brochure inside spread">
  <div class="page products">
    <h2 class="heading title">Our Products</h2>
    <p class="body-copy products-intro">Build the suit you want, piece by piece. Choose vests, shirts, pants, skirts and jackets, then add the details that make it yours.</p>
    <div class="photo round photo-shirt" role="img" aria-label="Photo of a man in a grey waistcoat and tie"></div>
    <div class="product product-1"><p class="label">PRODUCT 1</p><p class="body-copy">Canvas and half canvas suits that hold their shape and move with you through a long day.</p></div>
    <div class="product product-2"><p class="label">PRODUCT 2</p><p class="body-copy">Shirts cut to your collar and cuff, with an optional monogram stitched in the colour you pick.</p></div>
    <div class="photo round photo-shoes" role="img" aria-label="Photo of suit trousers and black leather shoes"></div>
    <div class="product product-3"><p class="label">PRODUCT 3</p><p class="body-copy">Vests and pants tailored to match, with horn buttons and clean pressed lines for a sharp finish.</p></div>
    <div class="product product-4"><p class="label">PRODUCT 4</p><p class="body-copy">Silk and paisley linings plus pocket squares add a quiet flash of colour to any suit.</p></div>
    <div class="fabric-box"><div class="fabric-box-inner">Available in Wool, cotton, linen, and a cotton /cashmere blend</div></div>
    <blockquote class="testimonial"><span class="mark">&ldquo;</span><p class="body-copy">My suit fit perfectly from the first try. Friends keep asking where I had it made.</p></blockquote>
  </div>

  <div class="page why">
    <div class="tagline"><div class="tagline-inner">Custom made suits make the wearer look amazing, as compared to an off the rack suit.</div></div>
    <div class="photo photo-seated" role="img" aria-label="Photo of a man in a blue shirt and tie sitting on the floor"></div>
    <h2 class="heading title">Why Choose Us?</h2>
    <div class="reason reason-1">
      <span class="reason-icon"><svg width="16" height="16" viewBox="0 0 16 16"><path d="M2 8.5l4 4 8-9" fill="none" stroke="#c51a4a" stroke-width="2.2" stroke-linecap="round" stroke-linejoin="round"/></svg></span>
      <p class="body-copy">Best value: a custom suit for a third of the local price.</p>
    </div>
    <div class="reason reason-2">
      <span class="reason-icon"><svg width="18" height="12" viewBox="0 0 18 12"><rect x="1" y="1" width="16" height="10" rx="1" fill="none" stroke="#c51a4a" stroke-width="1.5"/><circle cx="9" cy="6" r="2.2" fill="#c51a4a"/></svg></span>
      <p class="body-copy">Free measuring appointment and clear pricing with no hidden fees.</p>
    </div>
    <div class="reason reason-3">
      <span class="reason-icon"><svg width="16" height="16" viewBox="0 0 16 16"><path d="M5 1 1 4l2 3 1-1v9h8V6l1 1 2-3-4-3c-.5 1.5-1.6 2-3 2S5.5 2.5 5 1z" fill="#c51a4a"/></svg></span>
      <p class="body-copy">Wool, cotton, linen and cotton/cashmere blends in many colours.</p>
    </div>
    <div class="photo photo-couple" role="img" aria-label="Photo of a young man and woman in business suits"></div>
    <div class="cta">
      <div class="cta-inner">
        <p class="cta-lead">Call us to set up a free appointment to take your measurements!</p>
        <p class="cta-phone">604 555 0192</p>
      </div>
    </div>
  </div>
</section>

</body>
</html>
```